Website Design: Business to Business Coaching/Strategy

DO NOT CONTACT ME PRIVATELY. ANY PRIVATE CONTACT WILL BE IGNORED.

I need a website design for a business to business coaching service.

The website is for a company the specializes in coaching/training for other businesses. The business specializes in business development and human resource management.

Where appropriate, please include calls to action, e.g.: book a service & request a quote

CONTENT (SEEE ATTACHMENT)
5 Pages;
1. Home Page with overview of company/services -> Slide show at the top with tagline:

WE HELP MAKE STRATEGY HAPPEN BY

DELIVERING LONG-TERM PERFORMANCE IMPROVEMENTS

SO COMPANIES CAN

"BECOME THE CHANGE THEY WISH TO SEE."

2. Works - core services; coaching; leadership development, workshops
3. Expertise
a. capability: helping people to help themselves
b. company interventions: working in partnership; team facilitation; …
c. testimonials
4. About Us
5. Inquires
a. business capability development and funding
b. Register / enrol for an open programme or workshop
c. client feedback

The website below provides services that are similar to the services of my company: https://www.velcormo.co.uk

DESIGN
- Dark theme matching this style of website BUT a simpler more straightforward design: https://www.duntalwick.ac.uk/
Another theme that I like - Dark themed with a modern/easy design: https://lorpaskins.com/theme-demos/?demo=glimvera-dark

Target Market(s)

Small businesses

Industry/Entity Type

Executive training/business coaching

Number of Pages Required

5+ page

Colors

Designer to choose colors to be used in the design.

```html
<!DOCTYPE html>
<html lang="en">
<head>
<meta charset="utf-8">
<title>Veloria — Business Coaching &amp; Strategy</title>
<link href="https://fonts.googleapis.com/css2?family=Poppins:wght@400;500;600;700&display=swap" rel="stylesheet">
<style>
:root{
  --bg:#141215;
  --panel:#252326;
  --frame:#2a282b;
  --teal:#1a939d;
  --teal-bright:#1fb3c4;
  --orange:#f47b20;
  --white:#ffffff;
  --muted:#d9d9d9;
}
*{margin:0;padding:0;box-sizing:border-box}
html,body{width:1200px;height:3878px;overflow:hidden}
body{background:var(--bg);color:var(--white);font-family:'Poppins',sans-serif;position:relative}
.abs{position:absolute}
.photo{position:absolute}
/* Hero */
.hero{left:0;top:0;width:1200px;height:775px;background:linear-gradient(160deg,#7d7f82 0%,#55575b 40%,#3b3a3c 75%,#2b2826 100%)}
.hero::after{content:"";position:absolute;inset:0;background:rgba(0,0,0,.25)}
.nav{position:absolute;left:0;top:0;width:1200px;height:130px;z-index:2}
.logo{position:absolute;left:75px;top:60px;font-size:39px;font-weight:600;line-height:1;letter-spacing:.5px}
.nav-link{position:absolute;top:72px;font-size:19px;line-height:1;color:var(--white);text-decoration:none}
.nav-link.active{color:var(--orange);font-weight:600}
.nav-link.active::after{content:"";position:absolute;left:-12px;right:-10px;top:30px;height:3px;background:var(--orange)}
.quote-btn{position:absolute;left:929px;top:63px;width:196px;height:46px;border:2px solid var(--white);font-size:19px;display:flex;align-items:center;justify-content:center}
.hero-text{position:absolute;left:0;top:308px;width:1200px;text-align:center;z-index:2;font-weight:700;font-size:42px;line-height:48px;text-transform:uppercase;letter-spacing:.3px}
.hero-text .tag{color:var(--teal-bright);margin-top:6px;display:block}
.hero-arrow{position:absolute;top:390px;z-index:2}
/* Services */
.services-panel{left:0;top:867px;width:584px;height:359px;background:var(--panel)}
.card{position:absolute;top:914px;width:193px}
.card .img{width:193px;height:193px;border-radius:22px;position:relative;overflow:hidden}
.card .go{position:absolute;right:0;bottom:0;width:54px;height:54px;background:var(--orange);display:flex;align-items:center;justify-content:center;border-radius:0 0 22px 0}
.card h3{margin-top:14px;font-size:24px;font-weight:600;line-height:33px}
/* Works */
.works-frame{left:0;top:1370px;width:766px;height:617px;background:var(--frame)}
.works-photo{left:0;top:1350px;width:745px;height:613px;background:linear-gradient(135deg,#9aa0a3,#5f666b 55%,#3a3f44)}
.works-box{left:524px;top:1412px;width:602px;height:488px;background:var(--teal);padding:40px 0 0 33px}
.works-box h2{font-size:51px;font-weight:500;line-height:1}
.works-list{list-style:none;margin-top:20px}
.works-list li{display:flex;align-items:center;height:63px;font-size:33px;font-weight:500}
.works-list svg{margin-right:38px}
.outline-btn{display:flex;align-items:center;justify-content:center;border:2px solid var(--white);font-size:17px;font-weight:500;color:var(--white)}
.works-box .outline-btn{position:absolute;left:33px;top:390px;width:187px;height:50px}
/* Expertise */
.section-title{left:0;width:1200px;text-align:center;font-size:51px;font-weight:500}
.subtitle{left:0;width:1200px;text-align:center;font-size:24px}
.exp{position:absolute;top:2236px;width:330px}
.exp .img{width:328px;height:241px}
.exp h3{height:96px;display:flex;align-items:center;font-size:30px;font-weight:600;line-height:38px;margin-top:12px}
.exp p{font-size:16px;line-height:27.5px;color:var(--muted)}
.exp .btns{display:flex;gap:12px;margin-top:18px}
.orange-btn{width:154px;height:50px;border:2px solid var(--orange);display:flex;align-items:center;justify-content:center;font-size:17px;font-weight:500}
/* About */
.about-frame{left:435px;top:2868px;width:765px;height:629px;background:var(--frame)}
.about-photo{left:459px;top:2840px;width:741px;height:630px;background:linear-gradient(120deg,#c9ced3,#8d9096 45%,#4a4a50)}
.about-box{left:75px;top:2921px;width:601px;height:486px;background:var(--teal);padding:0 27px}
.about-box h2{margin-top:66px;font-size:54px;font-weight:500;line-height:1}
.about-box h4{margin-top:20px;font-size:25px;font-weight:400;line-height:33px}
.about-box p{margin-top:12px;font-size:16px;line-height:27.5px;width:520px}
.about-box .outline-btn{margin-top:28px;width:186px;height:50px}
/* Footer */
.footer-link{position:absolute;top:3680px;font-size:20px}
.copyright{left:73px;top:3734px;font-size:15px;line-height:28px;color:var(--muted)}
.social{position:absolute;top:3722px;width:24px;height:24px;background:var(--white);border-radius:50%}
</style>
</head>
<body>

<header class="abs hero">
  <div class="photo" role="img" aria-label="Photo of a businesswoman presenting to colleagues at a meeting table" style="inset:0"></div>
</header>
<nav class="nav">
  <div class="logo">Veloria</div>
  <a class="nav-link active" style="left:360px">Home</a>
  <a class="nav-link" style="left:461px">Works</a>
  <a class="nav-link" style="left:563px">Expertise</a>
  <a class="nav-link" style="left:691px">About Us</a>
  <a class="nav-link" style="left:821px">Inquires</a>
  <a class="quote-btn">Request a Quote</a>
</nav>
<h1 class="hero-text">We help make strategy happen<br>bydelivering long-term performance<br>improvements so companies can<span class="tag">"Become the change they wish to see."</span></h1>
<svg class="hero-arrow" style="left:42px" width="34" height="34" viewBox="0 0 34 34"><path d="M30 17H5M16 5L4 17l12 12" stroke="#fff" stroke-width="4" fill="none"/></svg>
<svg class="hero-arrow" style="left:1126px" width="34" height="34" viewBox="0 0 34 34"><path d="M4 17h25M18 5l12 12-12 12" stroke="#fff" stroke-width="4" fill="none"/></svg>

<section>
  <div class="abs services-panel"></div>
  <div class="card" style="left:75px"><div class="img" role="img" aria-label="Photo of a leader speaking to a seated team" style="background:linear-gradient(135deg,#d8dadc,#8b8f93)"><span class="go"><svg width="24" height="24" viewBox="0 0 24 24"><path d="M3 12h17M13 5l7 7-7 7" stroke="#fff" stroke-width="3" fill="none"/></svg></span></div><h3>Leadership &amp;<br>Capability</h3></div>
  <div class="card" style="left:289px"><div class="img" role="img" aria-label="Photo of screens showing analytics charts" style="background:linear-gradient(135deg,#c7ccd1,#4d5258)"><span class="go"><svg width="24" height="24" viewBox="0 0 24 24"><path d="M3 12h17M13 5l7 7-7 7" stroke="#fff" stroke-width="3" fill="none"/></svg></span></div><h3>Assessment<br>&amp; Analysis</h3></div>
  <div class="card" style="left:504px"><div class="img" role="img" aria-label="Photo of a team collaborating at a table" style="background:linear-gradient(135deg,#8f9aa3,#3f464d)"><span class="go"><svg width="24" height="24" viewBox="0 0 24 24"><path d="M3 12h17M13 5l7 7-7 7" stroke="#fff" stroke-width="3" fill="none"/></svg></span></div><h3>People &amp;<br>Engagement</h3></div>
  <div class="card" style="left:718px"><div class="img" role="img" aria-label="Photo of a magnifying glass over documents" style="background:linear-gradient(135deg,#e6e8ea,#8a8e93)"><span class="go"><svg width="24" height="24" viewBox="0 0 24 24"><path d="M3 12h17M13 5l7 7-7 7" stroke="#fff" stroke-width="3" fill="none"/></svg></span></div><h3>Investigate<br>&amp; Guide</h3></div>
  <div class="card" style="left:933px"><div class="img" role="img" aria-label="Photo of puzzle pieces on a chalkboard with a rising arrow" style="background:linear-gradient(135deg,#5a6570,#2c3339)"><span class="go"><svg width="24" height="24" viewBox="0 0 24 24"><path d="M3 12h17M13 5l7 7-7 7" stroke="#fff" stroke-width="3" fill="none"/></svg></span></div><h3>A Personalised<br>Approach</h3></div>
</section>

<section>
  <div class="abs works-frame"></div>
  <div class="abs works-photo" role="img" aria-label="Photo of a presenter at a whiteboard with an audience in a meeting room"></div>
  <div class="abs works-box">
    <h2>Works</h2>
    <ul class="works-list">
      <li><svg width="30" height="16" viewBox="0 0 30 16"><path d="M0 8h24M18 2l7 6-7 6" stroke="#111" stroke-width="4" fill="none"/></svg>Core services</li>
      <li><svg width="30" height="16" viewBox="0 0 30 16"><path d="M0 8h24M18 2l7 6-7 6" stroke="#111" stroke-width="4" fill="none"/></svg>Coaching</li>
      <li><svg width="30" height="16" viewBox="0 0 30 16"><path d="M0 8h24M18 2l7 6-7 6" stroke="#111" stroke-width="4" fill="none"/></svg>Leadership Development</li>
      <li><svg width="30" height="16" viewBox="0 0 30 16"><path d="M0 8h24M18 2l7 6-7 6" stroke="#111" stroke-width="4" fill="none"/></svg>Workshops</li>
    </ul>
    <a class="outline-btn">Book a Service</a>
  </div>
</section>

<section>
  <h2 class="abs section-title" style="top:2066px">Expertise</h2>
  <p class="abs subtitle" style="top:2157px">For leaders who believe focused development presents a competitive edge.</p>
  <div class="exp" style="left:75px"><div class="img" role="img" aria-label="Photo of a mentor guiding a colleague at a computer" style="background:linear-gradient(135deg,#cdd0d2,#6f7478)"></div><h3>Coaching<br>&amp; Mentoring</h3><p>Sed ut perspiciatis unde omnis iste natus error sit voluptatem accusantium doloremque pariatur.</p><div class="btns"><a class="orange-btn">Register Now</a><a class="orange-btn">Contact Us</a></div></div>
  <div class="exp" style="left:437px"><div class="img" role="img" aria-label="Photo of a confident business team standing together" style="background:linear-gradient(135deg,#a8b0b8,#4b5663)"></div><h3>Leadership</h3><p>Sed ut perspiciatis unde omnis iste natus error sit voluptatem accusantium doloremque pariatur.</p><div class="btns"><a class="orange-btn">Register Now</a><a class="orange-btn">Contact Us</a></div></div>
  <div class="exp" style="left:798px"><div class="img" role="img" aria-label="Photo of a trainer presenting at a whiteboard" style="background:linear-gradient(135deg,#d6dadd,#7b8085)"></div><h3>Training &amp;<br>Development</h3><p>Sed ut perspiciatis unde omnis iste natus error sit voluptatem accusantium doloremque pariatur.</p><div class="btns"><a class="orange-btn">Register Now</a><a class="orange-btn">Contact Us</a></div></div>
</section>

<section>
  <div class="abs about-frame"></div>
  <div class="abs about-photo" role="img" aria-label="Photo of two colleagues discussing work at a laptop"></div>
  <div class="abs about-box">
    <h2>About Us</h2>
    <h4>Helping businesses<br>achieve transformational change</h4>
    <p>Transformation is incredibly hard and like many businesses, we too have had to be adaptive and learn to become agile in how we engage organisations and add value in a sustainable way.</p>
    <a class="outline-btn">Read More</a>
  </div>
</section>

<footer>
  <a class="footer-link" style="left:72px">Home</a>
  <a class="footer-link" style="left:172px">Works</a>
  <a class="footer-link" style="left:273px">Expertise</a>
  <a class="footer-link" style="left:402px">About Us</a>
  <a class="footer-link" style="left:531px">Inquires</a>
  <p class="abs copyright">Copyright © 2022. CompanyName.<br>All Right Reserved</p>
  <span class="social" style="left:903px" aria-label="Social link"></span>
  <span class="social" style="left:951px" aria-label="Social link"></span>
  <span class="social" style="left:1002px" aria-label="Social link"></span>
  <span class="social" style="left:1052px" aria-label="Social link"></span>
  <span class="social" style="left:1103px" aria-label="Social link"></span>
</footer>

</body>
</html>
```